Real Estate Entrepreneur needs a business card

I am a real estate entrepreneur, I buy houses for investment purposes, I act as a real estate agent representing buyers and sellers in residential home transactions, I am a contractor that does a wide range of home repairs and construction. I'd like a design that can stick with me through the years as my business grows and morphs to fit any niche I decide to pursue as markets change.

Target Market(s)

Anyone with interest that may be related to real estate.

Industry/Entity Type

Real Estate

Contact Information for Business Card

A card that stands out and doesn't put me in any one box. My business will evolve over time and I need a card that can stay relevant.

Colors

Designer to choose colors to be used in the design.

Requirements
Must have
• Character
Nice to have
• I'm open
Should not have
• Cliche houses and hammers

```html
<!DOCTYPE html>
<html lang="en">
<head>
<meta charset="UTF-8">
<title>Reid Halden — Business Card</title>
<link rel="stylesheet" href="https://fonts.googleapis.com/css2?family=Work+Sans:wght@400;500;600&display=swap">
<style>
  :root {
    --backdrop: #1c1c1c;
    --card-dark: #161616;
    --card-light: #ffffff;
    --ink: #1a1a1a;
    --wordmark: #9a9a9a;
    --rule: #333333;
  }
  * { margin: 0; padding: 0; box-sizing: border-box; }
  html, body {
    width: 1200px;
    height: 900px;
    overflow: hidden;
    background: var(--backdrop);
    font-family: "Work Sans", sans-serif;
  }
  .stage {
    width: 1200px;
    height: 900px;
    display: flex;
    flex-direction: column;
    align-items: center;
    justify-content: center;
    gap: 40px;
  }
  .card {
    width: 560px;
    height: 320px;
    display: flex;
    flex-direction: column;
    align-items: center;
    justify-content: center;
    box-shadow: 0 10px 30px rgba(0,0,0,0.45);
  }
  .card--front { background: var(--card-dark); }
  .card--back { background: var(--card-light); color: var(--ink); text-align: center; }

  .wordmark {
    font-weight: 600;
    font-size: 40px;
    letter-spacing: 0.12em;
    color: var(--wordmark);
  }
  .holder-name {
    font-weight: 500;
    font-size: 30px;
    letter-spacing: 0.12em;
  }
  .holder-role {
    font-size: 16px;
    letter-spacing: 0.14em;
    margin-top: 2px;
  }
  .divider {
    width: 80px;
    height: 1px;
    background: var(--rule);
    margin: 12px 0 14px;
  }
  .contact-list { list-style: none; }
  .contact-list li {
    font-size: 17px;
    letter-spacing: 0.14em;
    line-height: 1.6;
  }
</style>
</head>
<body>
  <main class="stage">
    <section class="card card--front">
      <div class="wordmark">REID HALDEN</div>
    </section>
    <section class="card card--back">
      <h1 class="holder-name">REID HALDEN</h1>
      <p class="holder-role">Director</p>
      <div class="divider"></div>
      <ul class="contact-list">
        <li>P : (03) 5550 1842</li>
        <li>E : info@reidhalden.com</li>
        <li>W : www.reidhalden.com</li>
      </ul>
    </section>
  </main>
</body>
</html>
```